Briefpapier klangrabatt17
Die Zusammenarbeit war vorbildlich. Sehr schnelle Reaktion auf unsere Wünsche und eine sehr gute Umsetzung des Projektes. Danke, wir werden wieder auf Sie zurückkommen für unseren nächsten Flyer.
Zielgruppe
Wir verkaufen Musiknoten, Lehr-DVDs für Instrumente aus Klassik, Rock, Pop, Jazz etc.
Da wir in letzter Zeit mehr Musiknoten aus der Klassik haben, wäre es sinnvoll, den Briefbogen seriös zu gestalten.
Aufgabenstellung
Wir bitten um Gestaltung eines Briefbogens mit den folgenden Informationen:
Anschrift: klangrabatt17
www.klangrabatt17.example
Wir haben folgende Homepage:
http://laden.tonfinder.example/38527/Home.html
Der Zusatz lyra digital sollte allerdings nicht im Brieflogo erscheinen.
Also Logo nur mit "klangrabatt17" und dem Zusatz: Ihr Spezialist für Musiknoten und Lehr-DVD's
Bitte die in der angefügten Datei verwandten Farben verwenden (gelb und rot)

```html
<!DOCTYPE html>
<html lang="de">
<head>
<meta charset="utf-8">
<title>Briefpapier klangrabatt17</title>
<link rel="stylesheet" href="https://fonts.googleapis.com/css2?family=Source+Sans+3:wght@400;700;800&display=swap">
<style>
  :root {
    --bg: #f7f7f7;
    --paper: #fcfcfc;
    --white: #ffffff;
    --yellow: #cdc614;
    --red: #a3282a;
    --red-bright: #c3262c;
    --green: #2f8a2a;
    --flap: #e8e6c3;
    --ink: #333333;
    --grey: #8a8a8a;
    --line: #8d8d8d;
  }
  * { margin: 0; padding: 0; box-sizing: border-box; }
  html, body { width: 1200px; height: 1000px; overflow: hidden; background: var(--bg); }
  body { position: relative; font-family: "Source Sans 3", sans-serif; color: var(--ink); }
  svg { display: block; }

  .letterhead {
    position: absolute; left: 29px; top: 111px; width: 533px; height: 753px;
    background: var(--paper); box-shadow: 3px 4px 8px rgba(0,0,0,.25); overflow: hidden;
  }
  .letterhead .side-bar { position: absolute; right: 0; top: 0; width: 13px; height: 100%; background: var(--yellow); }
  .letterhead .curves { position: absolute; left: 0; top: 0; }
  .wordmark { position: absolute; font-weight: 800; color: var(--red); line-height: 1; letter-spacing: -.5px; white-space: nowrap; }
  .letterhead .wordmark { right: 22px; top: 32px; font-size: 31px; }
  .contact { position: absolute; left: 398px; top: 84px; font-size: 7.8px; color: #444; }
  .contact li { list-style: none; display: flex; align-items: flex-start; gap: 6px; margin-bottom: 4.5px; line-height: 10px; white-space: nowrap; }
  .contact li:first-child { margin-bottom: 7px; }
  .contact .icon { width: 11px; height: 11px; flex: none; }
  .return-line { position: absolute; left: 121px; top: 146px; font-size: 7.6px; }
  .return-line .dot { display: inline-block; width: 4px; height: 4px; border-radius: 50%; background: var(--red-bright); margin: 0 2px 1px; }
  .fold-mark { position: absolute; left: 0; width: 20px; border-top: 1px solid var(--line); }
  .footer-bank { position: absolute; left: 96px; top: 710px; font-size: 6.8px; color: var(--grey); line-height: 8.5px; }
  .footer-legal { position: absolute; left: 330px; top: 715px; width: 145px; font-size: 6.8px; color: var(--grey); line-height: 8.5px; text-align: center; }

  .envelope { position: absolute; left: 600px; width: 560px; }
  .envelope .body { position: absolute; left: 0; width: 560px; background: var(--white); box-shadow: 2px 3px 6px rgba(0,0,0,.25); }
  .envelope-front { top: 133px; height: 384px; }
  .envelope-front .flap { position: absolute; left: 0; top: 0; }
  .envelope-front .body { top: 98px; height: 286px; border-top: 1.5px solid var(--line); }
  .sender { position: absolute; left: 29px; top: 40px; display: flex; gap: 5px; font-size: 8px; line-height: 10px; color: var(--grey); }
  .sender .name { color: var(--red-bright); }
  .window { position: absolute; left: 39px; top: 155px; width: 223px; height: 88px; border-radius: 12px; background: var(--white); box-shadow: inset 2px 2px 4px rgba(0,0,0,.3); }
  .envelope-front .wordmark { right: 28px; top: 199px; font-size: 34px; }
  .envelope-front .curves { position: absolute; left: 0; top: 0; }
  .envelope-back { top: 538px; height: 291px; }
  .envelope-back .body { top: 0; height: 291px; }
  .envelope-back .flap { position: absolute; left: 0; top: 0; }

  .spare-strip { position: absolute; left: 407px; top: 946px; width: 184px; height: 10px; background: var(--flap); clip-path: polygon(0 0, 100% 0, 100% 100%, 4% 100%); }
</style>
</head>
<body>

<section class="letterhead">
  <svg class="curves" width="533" height="753" viewBox="0 0 533 753">
    <path d="M0 27 Q131 72 254 27" fill="none" stroke="var(--yellow)" stroke-width="3"/>
    <path d="M254 27 Q391 -27 533 27" fill="none" stroke="var(--red)" stroke-width="3"/>
    <path d="M0 728 Q141 680 280 727" fill="none" stroke="var(--red)" stroke-width="3"/>
    <path d="M280 727 Q404 775 520 733" fill="none" stroke="var(--yellow)" stroke-width="3"/>
  </svg>
  <div class="side-bar"></div>
  <div class="wordmark">klangrabatt17</div>

  <ul class="contact">
    <li>
      <svg class="icon" viewBox="0 0 12 12"><circle cx="6" cy="6" r="6" fill="var(--red)"/><path d="M6 2.3a2.4 2.4 0 0 0-2.4 2.4C3.6 6.6 6 9.6 6 9.6s2.4-3 2.4-4.9A2.4 2.4 0 0 0 6 2.3z" fill="#fff"/><circle cx="6" cy="4.7" r=".9" fill="var(--red)"/></svg>
      <span>Ahornweg 8<br>85099 Musterdorf</span>
    </li>
    <li>
      <svg class="icon" viewBox="0 0 12 12"><circle cx="6" cy="6" r="6" fill="var(--red)"/><path d="M2.6 5.2c0-1.4 6.8-1.4 6.8 0v.6H7.9v-.7H4.1v.7H2.6z M3.6 6.3h4.8l.6 2.6H3z" fill="#fff"/></svg>
      <span>01234-56780</span>
    </li>
    <li>
      <svg class="icon" viewBox="0 0 12 12"><circle cx="6" cy="6" r="6" fill="var(--red)"/><rect x="3.3" y="3" width="5.4" height="6.2" rx=".6" fill="none" stroke="#fff" stroke-width=".9"/><path d="M4.4 4.8h3.2M4.4 6.2h3.2M4.4 7.6h2" stroke="#fff" stroke-width=".7"/></svg>
      <span>01234-56789</span>
    </li>
    <li>
      <svg class="icon" viewBox="0 0 12 12"><circle cx="6" cy="6" r="6" fill="var(--red)"/><text x="6" y="8.6" font-size="8" text-anchor="middle" fill="#fff" font-family="sans-serif">@</text></svg>
      <span>info@klangrabatt17.example</span>
    </li>
    <li>
      <svg class="icon" viewBox="0 0 12 12"><circle cx="6" cy="6" r="6" fill="var(--red)"/><circle cx="6" cy="6" r="3" fill="none" stroke="#fff" stroke-width=".9"/><path d="M3 6h6M6 3v6" stroke="#fff" stroke-width=".7"/></svg>
      <span>www.klangrabatt17.example</span>
    </li>
  </ul>

  <p class="return-line">Ahornweg 8 <span class="dot"></span>85099 Musterdorf</p>
  <div class="fold-mark" style="top:263px"></div>
  <div class="fold-mark" style="top:501px"></div>

  <p class="footer-bank">Bankverbindung:<br>Bernd Haller Sparkasse Musterstadt<br>BIC:&nbsp;&nbsp;&nbsp; MUSTDEX1XXX<br>IBAN: DE00 1234 5678 9012 3456 78</p>
  <p class="footer-legal">Geschäftsführer: Bernd Haller<br>Steuernummer: 000-111-22233<br>UST-ID-Nr. DE 000000000</p>
</section>

<section class="envelope envelope-front">
  <svg class="flap" width="560" height="99" viewBox="0 0 560 99">
    <path d="M0 99 L0 70 Q0 55 30 48 L255 2 Q277 -2 299 2 L530 48 Q560 55 560 70 L560 99 Z" fill="var(--flap)"/>
  </svg>
  <div class="body">
    <div class="sender">
      <svg width="12" height="18" viewBox="0 0 12 18"><path d="M6 0a5.5 5.5 0 0 0-5.5 5.5C.5 10 6 17 6 17s5.5-7 5.5-11.5A5.5 5.5 0 0 0 6 0z" fill="var(--yellow)"/><circle cx="6" cy="5.5" r="2" fill="#fff"/></svg>
      <p><span class="name">Bernd Haller</span><br>Ahornweg 8<br>85099 Musterdorf</p>
    </div>
    <div class="window"></div>
    <div class="wordmark">klangrabatt17</div>
    <svg class="curves" width="560" height="286" viewBox="0 0 560 286">
      <path d="M0 265 Q150 235 297 266" fill="none" stroke="var(--green)" stroke-width="2"/>
      <path d="M297 266 Q423 295 560 260" fill="none" stroke="var(--red-bright)" stroke-width="2"/>
    </svg>
  </div>
</section>

<section class="envelope envelope-back">
  <div class="body"></div>
  <svg class="flap" width="560" height="101" viewBox="0 0 560 101">
    <path d="M0 0 L0 28 Q0 43 30 51 L255 98 Q277 102 299 98 L530 51 Q560 43 560 28 L560 0 Z" fill="var(--flap)"/>
  </svg>
</section>

<div class="spare-strip"></div>

</body>
</html>
```